WordPress Site Design and Code for Technology Consulting Startup

We need a WordPress design and code to a new site on Nimbo Vault. We have the logo and colors ready. The site will be a brochure site with a CONTACT page that contains a form that the prospective client fills out. The other pages would be ABOUT / SERVICES (3 option drop-down) / SUPPORT. The site should be appropriate for an IT Consulting / IT Managed Services / IT Project Management services in the Chicago area.

Target Market(s)

Across small, medium, large businesses.

Industry/Entity Type

Technology, network infrastructure, IT.

Coding

Coded - Design and coding required

Number of Pages Required

5+ page

Requirements
Nice to have
• I prefer mid-modern / simple / art deco / minimalist.

```html
<!DOCTYPE html>
<html lang="en">
<head>
<meta charset="UTF-8">
<title>Tessora — IT Consulting</title>
<link href="https://fonts.googleapis.com/css2?family=Syncopate:wght@400;700&family=Poppins:wght@400;500;600&family=Lato:wght@400&display=swap" rel="stylesheet">
<style>
:root{
  --teal:#1f93ae;
  --teal-dark:#16809a;
  --orange:#f47a20;
  --ink:#1d1d1f;
  --text:#2b2b2b;
  --peach:#fdf1e7;
  --field:#e4e4e4;
  --white:#ffffff;
}
*{margin:0;padding:0;box-sizing:border-box}
html,body{width:1200px;height:3423px;overflow:hidden;background:var(--white)}
body{position:relative;font-family:"Poppins",sans-serif;color:var(--text)}
.abs{position:absolute}
.display{font-family:"Syncopate",sans-serif;font-weight:700;text-transform:uppercase;letter-spacing:2px}
.btn{position:absolute;display:flex;align-items:center;justify-content:center;background:var(--orange);color:var(--white);font-family:"Syncopate",sans-serif;font-weight:700;font-size:15px;letter-spacing:2px;text-transform:uppercase}
.btn-sm{font-family:"Poppins",sans-serif;font-weight:600;font-size:16px;letter-spacing:0}

/* header */
.site-header{left:0;top:0;width:1200px;height:80px;background:var(--white)}
.brand{display:flex;align-items:center;gap:10px;font-family:"Syncopate",sans-serif;font-weight:700;letter-spacing:1px}
.brand-mark{width:22px;height:22px}
.header-brand{left:74px;top:22px;color:var(--teal);font-size:28px}
.header-brand .brand-mark{background:var(--orange)}
.main-nav{left:0;top:34px;width:1200px;height:20px;font-family:"Syncopate",sans-serif;font-weight:700;font-size:13px;letter-spacing:1px;color:var(--ink)}
.main-nav span{position:absolute;top:0}
.main-nav .active{color:var(--teal)}

/* hero */
.hero{left:0;top:80px;width:1200px;height:659px;background:linear-gradient(110deg,#2b3040 0%,#2e4a6e 45%,#3b6fa6 70%,#1e3558 100%)}
.hero-title{right:74px;top:265px;text-align:right;color:var(--white);font-size:64px;line-height:67px;letter-spacing:4px}
.hero-sub{right:74px;top:405px;width:640px;text-align:right;color:var(--white);font-size:23px;line-height:33px}
.dots{left:562px;top:681px;display:flex;gap:12px}
.dots i{display:block;width:13px;height:13px;border-radius:50%;background:var(--white)}
.dots i.on{background:var(--teal)}

/* about */
.about-peach{left:0;top:817px;width:435px;height:588px;background:linear-gradient(135deg,#ffffff 0%,var(--peach) 100%)}
.about-title{left:74px;top:812px;font-size:44px;line-height:48px;color:var(--ink);letter-spacing:3px}
.about-title .accent{color:var(--teal)}
.about-copy{left:74px;top:929px;width:332px;font-size:15.5px;line-height:27.7px;color:var(--ink)}
.about-copy p+p{margin-top:6px}
.about-photo{left:435px;top:817px;width:765px;height:588px;background:linear-gradient(120deg,#1b2b3e 0%,#3c5f80 50%,#243a55 100%)}

/* services */
.services-band{left:-260px;top:1508px;width:1720px;height:721px;background:var(--teal);border-radius:50% 50% 0 0 / 170px 170px 0 0}
.services-title{left:0;top:1618px;width:1200px;text-align:center;color:var(--white);font-size:44px;letter-spacing:3px}
.service{position:absolute;top:1724px;text-align:center;color:var(--white)}
.service svg{display:block;margin:0 auto}
.service h3{font-family:"Syncopate",sans-serif;font-weight:700;font-size:21px;line-height:27px;letter-spacing:2px;text-transform:uppercase;margin-top:38px}
.service p{font-size:17.5px;line-height:30.5px;margin-top:10px}
.divider{top:1710px;width:1px;height:387px;background:rgba(255,255,255,.7)}

/* support */
.support{left:74px;top:2168px;width:1053px;height:430px;background:linear-gradient(90deg,#4a4646 0%,#6a5f5a 45%,#3f3d3f 100%);border-radius:0 0 50% 50% / 0 0 120px 120px}
.support-title{left:0;top:2250px;width:1200px;text-align:center;color:var(--white);font-size:44px;letter-spacing:3px}
.support-copy{left:180px;top:2320px;width:840px;text-align:center;color:var(--white);font-size:15px;line-height:29.5px}

/* contact */
.contact-deco{left:767px;top:2665px;width:433px;height:600px;background:linear-gradient(160deg,#eaf5f8 0%,#ffffff 70%)}
.contact-photo{left:0;top:2665px;width:767px;height:587px;background:linear-gradient(120deg,#cfc7bb 0%,#8e8477 50%,#5a5048 100%)}
.contact-card{left:615px;top:2731px;width:545px;height:455px;background:var(--white)}
.contact-title{left:652px;top:2768px;font-size:44px;color:var(--ink);letter-spacing:3px}
.contact-title .accent{color:var(--teal)}
.field{position:absolute;background:var(--field);font-family:"Lato",sans-serif;font-size:17px;color:var(--ink);padding:16px 20px}

/* footer */
.site-footer{left:0;top:3313px;width:1200px;height:110px;background:var(--teal)}
.copyright{left:74px;top:3362px;color:var(--white);font-size:14px}
.footer-brand{left:0;top:3350px;width:1200px;justify-content:center;color:var(--white);font-size:26px}
.footer-brand .brand-mark{background:var(--white)}
.follow{left:933px;top:3340px;color:var(--white);font-family:"Syncopate",sans-serif;font-weight:700;font-size:15px;letter-spacing:1px}
.social{left:933px;top:3377px;display:flex;gap:19px}
.social i{display:block;width:22px;height:22px;border-radius:50%;background:var(--white)}
</style>
</head>
<body>

<header class="abs site-header">
  <div class="abs brand header-brand"><span class="brand-mark"></span>Tessora</div>
  <nav class="abs main-nav">
    <span class="active" style="left:458px">Home</span>
    <span style="left:561px">About Us</span>
    <span style="left:712px">Services</span>
    <span style="left:856px">Support</span>
    <span style="left:997px">Contact Us</span>
  </nav>
</header>

<section>
  <div class="abs hero" role="img" aria-label="Two IT engineers with a laptop in a server room, overlaid with glowing cloud network graphics"></div>
  <h1 class="abs display hero-title">Welcome to<br>Tessora</h1>
  <p class="abs hero-sub">Sed ut perspiciatis unde omnis iste natus error sit voluptatem accusantiumdoloremque.</p>
  <a class="btn" style="left:918px;top:488px;width:209px;height:53px">Read More</a>
  <div class="abs dots"><i class="on"></i><i></i><i></i><i></i></div>
</section>

<section>
  <div class="abs about-peach"></div>
  <h2 class="abs display about-title">About<br><span class="accent">Tessora</span></h2>
  <div class="abs about-copy">
    <p>Sed ut perspiciatis unde omnis iste natus error sit voluptatem accusantium doloremque laudantium, totam rem aperiam, eaque ipsa quae ab illo inventore veritatis et quasi architecto beatae vitae dicta sunt explicaboemo enim ipsam voluptatem quia voluptas sit aspernatur aut odit aut fugit, sed quia consequuntur magni dolores eos qui ratione voluptatem sequi nesciunt.</p>
    <p>Neque porro quisquam est, qui dolorem ipsum quia dolor sit amet, consectetur, adipisci velit, sed quia non numquam eius modi tempora incidunt ut labore</p>
  </div>
  <a class="btn" style="left:74px;top:1352px;width:209px;height:53px">Read More</a>
  <div class="abs about-photo" role="img" aria-label="Two colleagues in a data centre reviewing a laptop showing the company name"></div>
</section>

<section>
  <div class="abs services-band"></div>
  <h2 class="abs display services-title">Our Services</h2>

  <div class="service" style="left:70px;width:330px">
    <svg width="74" height="72" viewBox="0 0 74 72" fill="none" stroke="#fff" stroke-width="2.2">
      <circle cx="37" cy="22" r="12"/><circle cx="37" cy="22" r="5"/>
      <path d="M37 4v6M37 34v6M19 22h6M49 22h6"/>
      <circle cx="12" cy="44" r="6"/><path d="M2 70v-8a10 10 0 0 1 20 0v8z"/>
      <circle cx="62" cy="44" r="6"/><path d="M52 70v-8a10 10 0 0 1 20 0v8z"/>
      <path d="M28 50h18v20H28z"/>
    </svg>
    <h3>IT Consulting</h3>
    <p>Nemo enim ipsam voluptatem quia voluptas sit aspernatur aut odit aut fugit, sed quia consequuntur magni dolores eos.</p>
  </div>
  <a class="btn btn-sm" style="left:162px;top:2013px;width:143px;height:44px">LEARN MORE</a>

  <div class="abs divider" style="left:420px"></div>

  <div class="service" style="left:436px;width:328px">
    <svg width="74" height="72" viewBox="0 0 74 72" fill="none" stroke="#fff" stroke-width="2.2">
      <path d="M4 16h40M4 16v38h62V36"/><path d="M26 54v10M16 64h24"/>
      <circle cx="52" cy="18" r="11"/><circle cx="52" cy="18" r="4"/>
      <path d="M52 3v4M52 29v4M37 18h4M63 18h4"/><path d="M10 46h30"/>
    </svg>
    <h3>IT Managed<br>Services</h3>
    <p>Nemo enim ipsam voluptatem quia voluptas sit aspernatur aut odit aut fugit, sed quia con.</p>
  </div>
  <a class="btn btn-sm" style="left:528px;top:2013px;width:143px;height:44px">LEARN MORE</a>

  <div class="abs divider" style="left:780px"></div>

  <div class="service" style="left:796px;width:332px">
    <svg width="74" height="72" viewBox="0 0 74 72" fill="none" stroke="#fff" stroke-width="2.2">
      <rect x="4" y="2" width="54" height="66"/><path d="M4 16h54"/>
      <rect x="12" y="24" width="20" height="12"/><path d="M12 44h24M12 52h20M12 60h16"/>
      <circle cx="58" cy="52" r="10"/><circle cx="58" cy="52" r="4"/>
    </svg>
    <h3>IT Project<br>Management<br>Services</h3>
    <p>Nemo enim ipsam voluptatem quia voluptas sit aspernatur aut odit aut fugit, sed quia con.</p>
  </div>
  <a class="btn btn-sm" style="left:891px;top:2025px;width:143px;height:44px">LEARN MORE</a>
</section>

<section>
  <div class="abs support" role="img" aria-label="Support agent with a headset working at a computer in an office"></div>
  <h2 class="abs display support-title">Support</h2>
  <p class="abs support-copy">Sed ut perspiciatis unde omnis iste natus error sit voluptatem accusantium doloremque laudantium, totam rem&nbsp; aperiam, eaque ipsa quae ab illo inventore veritatis et quasi architecto beatae vitae dicta sunt explicaboemo enimipsam voluptatem quia voluptas sit aspernatur aut odit.</p>
  <a class="btn" style="left:496px;top:2432px;width:208px;height:52px">Read More</a>
</section>

<section>
  <div class="abs contact-deco"></div>
  <div class="abs contact-photo" role="img" aria-label="Man in glasses thinking while working on a laptop in a bright office"></div>
  <div class="abs contact-card"></div>
  <h2 class="abs display contact-title">Contact <span class="accent">Us</span></h2>
  <div class="field" style="left:652px;top:2836px;width:231px;height:53px">Name</div>
  <div class="field" style="left:896px;top:2836px;width:231px;height:53px">Email Address</div>
  <div class="field" style="left:652px;top:2901px;width:231px;height:52px">Phone No</div>
  <div class="field" style="left:896px;top:2901px;width:231px;height:52px">Subject</div>
  <div class="field" style="left:652px;top:2966px;width:475px;height:107px">Message</div>
  <a class="btn" style="left:652px;top:3087px;width:209px;height:52px">Submit</a>
</section>

<footer class="abs site-footer"></footer>
<p class="abs copyright">Copyright © 2023 Tessora All Right Reserved</p>
<div class="abs brand footer-brand"><span class="brand-mark"></span>Tessora</div>
<p class="abs follow">Follow Us</p>
<div class="abs social"><i></i><i></i><i></i><i></i><i></i></div>

</body>
</html>
```